ALL TEXT GRAPHICS TM May 2025 for Instagram

We are looking for a series of social media graphics for Instagram (new size: 4:5 (1080 x 1350 pixels) ratio that are ALL TEXT. We want the following quotes below on each graphic; one quote per graphic. AND, In very small letters at the bottom of each graphic, add @TovaMarshOnline
The look and feel of these graphics should be complimentary to the color palette attached below; but keep them simple. But the design is up to you; at the end of this document, I provided various samples of all text graphics that I like as examples.
Target Market(s)
women looking to lose weight
Look and feel

```html
<!DOCTYPE html>
<html lang="en">
<head>
<meta charset="utf-8">
<title>All Text Graphics — TM</title>
<link href="https://fonts.googleapis.com/css2?family=Roboto+Slab:wght@500&family=Arimo:wght@700&family=Archivo+Narrow:wght@700&family=Poppins:wght@500;600&family=Playfair+Display:wght@400;800&family=Libre+Baskerville&display=swap" rel="stylesheet">
<style>
  :root {
    --page: #ffffff;
    --card: #ffffff;
    --ink: #333333;
    --muted: #7a7a7a;
    --magenta: #cc0066;
    --pink: #ff6eb4;
  }
  * { margin: 0; padding: 0; box-sizing: border-box; }
  html, body {
    width: 1200px;
    height: 1200px;
    overflow: hidden;
    background: var(--page);
  }
  .canvas { position: relative; width: 1200px; height: 1200px; }
  .post {
    position: absolute;
    top: 60px;
    width: 418px;
    height: 523px;
    background: var(--card);
    box-shadow: 0 0 14px rgba(0, 0, 0, 0.06);
    overflow: hidden;
  }
  .post--secret { left: 169px; }
  .post--thirties { left: 620px; }

  .slab-layer {
    position: absolute;
    inset: 0;
    width: 418px;
    height: 523px;
  }
  .slab {
    font-family: "Roboto Slab", serif;
    font-weight: 500;
    fill: var(--ink);
  }

  .line {
    position: absolute;
    left: 0;
    width: 100%;
    text-align: center;
    line-height: 1;
    white-space: nowrap;
  }
  .sans { font-family: "Poppins", sans-serif; color: var(--ink); }
  .display {
    font-family: "Playfair Display", serif;
    font-weight: 800;
    color: var(--pink);
    font-variant-numeric: lining-nums;
  }

  /* Post 1 */
  .secret-audience {
    top: 63px;
    font-family: "Arimo", sans-serif;
    font-weight: 700;
    font-size: 42px;
    color: var(--magenta);
    padding-left: 4px;
  }
  .secret-outcome { top: 102px; font-size: 27.5px; font-weight: 600; padding-left: 4px; }
  .secret-promise { top: 178px; font-size: 58px; line-height: 0.82; letter-spacing: -4px; }
  .secret-keyword {
    top: 350px;
    font-family: "Playfair Display", serif;
    font-weight: 400;
    font-size: 59px;
    letter-spacing: 1px;
    color: var(--magenta);
  }
  .secret-tail { top: 403px; font-size: 30px; font-weight: 500; }

  /* Post 2 */
  .thirties-warning {
    top: 91px;
    font-family: "Archivo Narrow", sans-serif;
    font-weight: 700;
    font-size: 47.5px;
    color: var(--magenta);
  }
  .thirties-answer { top: 200px; font-size: 35px; font-weight: 600; line-height: 1.03; }
  .thirties-result { top: 325px; font-size: 46px; letter-spacing: -3.5px; }
  .thirties-time { top: 410px; font-size: 46px; letter-spacing: -3.4px; }

  .handle {
    position: absolute;
    left: 0;
    width: 100%;
    top: 489px;
    text-align: center;
    font-family: "Libre Baskerville", serif;
    font-size: 13px;
    line-height: 1;
    letter-spacing: 1.3px;
    color: var(--muted);
    text-transform: uppercase;
  }
</style>
</head>
<body>
<main class="canvas">
  <section class="post post--secret">
    <svg class="slab-layer" viewBox="0 0 418 523" aria-hidden="false">
      <text class="slab" x="30" y="65" font-size="44" textLength="272" lengthAdjust="spacingAndGlyphs">This is the secret</text>
      <text class="slab" x="146" y="352" font-size="36" textLength="132" lengthAdjust="spacingAndGlyphs">COMMENT</text>
    </svg>
    <p class="line secret-audience">WOMEN OVER 40</p>
    <p class="line sans secret-outcome">are using to get snatched</p>
    <p class="line display secret-promise">WITHOUT<br>STARVING</p>
    <p class="line secret-keyword">SKINNY</p>
    <p class="line sans secret-tail">to get the exact plan</p>
    <p class="handle">@TovaMarshOnline</p>
  </section>

  <section class="post post--thirties">
    <svg class="slab-layer" viewBox="0 0 418 523">
      <text class="slab" x="22.5" y="84" font-size="44" textLength="371" lengthAdjust="spacingAndGlyphs">What worked in your 30s</text>
      <text class="slab" x="200" y="405" font-size="32" textLength="23" lengthAdjust="spacingAndGlyphs">in</text>
    </svg>
    <p class="line thirties-warning">WON’T WORK NOW</p>
    <p class="line sans thirties-answer">Here’s what<br>actually does.</p>
    <p class="line display thirties-result">DROP 30 POUNDS</p>
    <p class="line display thirties-time">3 MONTHS.</p>
    <p class="handle">@TovaMarshOnline</p>
  </section>
</main>
</body>
</html>
```